Flyers

Modify Existing Flyer and create another for exterior company
Updates

Previous Brief has been updated- we want to update this existing one also

Target Market(s)

Exterior Remodeling Customers

Industry/Entity Type

Remodeling/Construction

```html
<!DOCTYPE html>
<html lang="en">
<head>
<meta charset="utf-8">
<title>Northgate Roofing and Exteriors – Flyer</title>
<link rel="stylesheet" href="https://fonts.googleapis.com/css2?family=Poppins:ital,wght@0,400;0,500;0,600;0,700;1,700&display=swap">
<style>
  :root{
    --orange:#ee5a22;
    --blue:#1a72c9;
    --ink:#2c2c2c;
    --paper-top:#f6f6f6;
    --paper-bottom:#e4e4e4;
  }
  *{box-sizing:border-box;margin:0;padding:0}
  html,body{width:980px;height:1200px;overflow:hidden}
  body{font-family:'Poppins',sans-serif;color:var(--ink);background:#fff}
  .flyer{position:relative;width:980px;height:1200px;overflow:hidden;
    background:linear-gradient(180deg,var(--paper-top) 0%,#eeeeee 55%,var(--paper-bottom) 100%)}
  .abs{position:absolute}

  .hero-shape{position:absolute;left:0;top:0}

  .brand{left:34px;top:62px;display:flex;align-items:center;gap:10px}
  .brand-mark{width:16px;height:16px;background:var(--orange)}
  .brand-name{font-weight:600;font-size:21px;line-height:1.15;color:var(--orange);letter-spacing:.3px;width:260px}

  .cta{left:600px;top:33px;width:345px;text-align:right;font-weight:600;font-size:15.5px;letter-spacing:.2px;color:var(--ink)}
  .phone-pill{left:630px;top:59px;width:315px;height:46px;border:2.5px solid var(--blue);border-radius:24px;background:#fff}
  .phone-icon{position:absolute;left:-2px;top:-2px;width:46px;height:46px;border-radius:50%;background:var(--blue);display:flex;align-items:center;justify-content:center}
  .phone-number{position:absolute;left:56px;top:0;line-height:42px;font-weight:700;font-size:34px;color:var(--orange);letter-spacing:.3px}
  .website{left:680px;top:120px;width:265px;display:flex;justify-content:flex-end;align-items:center;gap:8px;font-size:14px;color:var(--ink)}

  .intro{left:221px;top:239px;font-size:13px;line-height:16px;color:var(--ink);text-transform:uppercase}
  .headline{left:136px;top:270px;font-weight:700;font-size:53px;line-height:56px;color:var(--orange);letter-spacing:.2px}

  .tab{height:33px;line-height:33px;font-weight:700;font-size:22px;color:#fff}
  .tab-left{left:0;padding-left:34px;border-radius:0 18px 18px 0}
  .tab-right{right:0;padding-right:33px;text-align:right;border-radius:18px 0 0 18px}
  .tab-blue{background:var(--blue)}
  .tab-orange{background:var(--orange)}

  .body-text{font-size:12.6px;line-height:16.4px;color:var(--ink)}
  .body-left{left:34px;width:214px}
  .body-right{right:33px;width:200px;text-align:right}

  .photo{border:2px solid var(--blue)}
  .photo.orange{border-color:var(--orange)}

  .checks{list-style:none;font-weight:600;font-size:12.8px;line-height:15.5px}
  .checks li{display:flex;gap:8px;margin-bottom:5px}
  .checks svg{flex:none;width:13px;height:13px;margin-top:1px}
  .checks.blue{color:var(--blue)}
  .checks.orange{color:var(--orange)}
</style>
</head>
<body>
<main class="flyer">
  <svg width="0" height="0" style="position:absolute">
    <defs>
      <symbol id="tick" viewBox="0 0 16 16">
        <circle cx="8" cy="8" r="8" fill="currentColor"/>
        <path d="M4.3 8.3l2.4 2.4 5-5" fill="none" stroke="#fff" stroke-width="2" stroke-linecap="round" stroke-linejoin="round"/>
      </symbol>
    </defs>
  </svg>

  <svg class="hero-shape" width="980" height="1200" viewBox="0 0 980 1200">
    <defs>
      <linearGradient id="heroTone" x1="0" y1="0" x2="1" y2="1">
        <stop offset="0" stop-color="#c9d0da"/>
        <stop offset=".45" stop-color="#9aa1ab"/>
        <stop offset="1" stop-color="#3b3e45"/>
      </linearGradient>
    </defs>
    <polygon role="img" aria-label="Photo of a roofer in a hard hat fitting standing-seam metal roof panels beside a chimney"
      points="535,93 980,406 980,506 527,841 0,590 0,325" fill="url(#heroTone)"/>
    <polyline points="5,314 535,71 980,402" fill="none" stroke="var(--blue)" stroke-width="6"/>
    <polyline points="9,605 519,848 980,517" fill="none" stroke="var(--orange)" stroke-width="5"/>
  </svg>

  <div class="abs brand">
    <span class="brand-mark"></span>
    <span class="brand-name">NORTHGATE ROOFING AND EXTERIORS</span>
  </div>

  <p class="abs cta">CALL TODAY FOR YOUR FREE ESTIMATE</p>
  <div class="abs phone-pill">
    <span class="phone-icon">
      <svg width="22" height="22" viewBox="0 0 24 24"><path fill="#fff" d="M6.6 10.8a15 15 0 006.6 6.6l2.2-2.2a1 1 0 011-.25 11.4 11.4 0 003.6.6 1 1 0 011 1V20a1 1 0 01-1 1A17 17 0 013 4a1 1 0 011-1h3.5a1 1 0 011 1c0 1.25.2 2.45.6 3.6a1 1 0 01-.25 1z"/></svg>
    </span>
    <span class="phone-number">515-555-0142</span>
  </div>
  <div class="abs website">
    <svg width="16" height="16" viewBox="0 0 16 16"><circle cx="8" cy="8" r="7" fill="none" stroke="var(--orange)" stroke-width="1.6"/><path d="M1 8h14M8 1c-3 3.5-3 10.5 0 14M8 1c3 3.5 3 10.5 0 14" fill="none" stroke="var(--orange)" stroke-width="1.2"/></svg>
    <span>www.northgateroofing.com</span>
  </div>

  <p class="abs intro">Work with a top-rated local<br>remodeling company in Ankeny, IA</p>
  <h1 class="abs headline">ROOFING &amp; EXTERIOR<br>SPECIALIST</h1>

  <!-- Roofing -->
  <h2 class="abs tab tab-left tab-blue" style="top:704px;width:174px">ROOFING</h2>
  <p class="abs body-text body-left" style="top:753px">When it comes to roofing, we install, site manage, and support your roof with 24/7 emergency roofing services. We are your local, family-owned roofing and home improvement specialists. No job is too big or too small. Our expert team is standing by to help answer your questions.</p>
  <div class="abs photo" role="img" aria-label="Photo of a dark tile roof with a dormer" style="left:272px;top:738px;width:189px;height:100px;background:linear-gradient(160deg,#8fb3d8,#3c4a63 55%,#7f8a94)"></div>
  <ul class="abs checks blue" style="left:274px;top:861px;width:210px">
    <li><svg><use href="#tick"/></svg>Asphalt Shingle Roof</li>
    <li><svg><use href="#tick"/></svg>Tile Roof</li>
    <li><svg><use href="#tick"/></svg>Metal Roof</li>
    <li><svg><use href="#tick"/></svg>Residential or Commercial Flat Roof</li>
  </ul>

  <!-- Siding -->
  <h2 class="abs tab tab-right tab-orange" style="top:704px;width:173px">SIDING</h2>
  <p class="abs body-text body-right" style="top:753px">Siding products, available in either cedar wood grain or smooth textures to beautify and protect your home. Enjoy decades of maintenance-free, stylish functionality that reflects your personality and improves your home’s look and appeal. Home siding is now a 21st century products.</p>
  <div class="abs photo orange" role="img" aria-label="Photo of grey vertical siding with white gable trim" style="left:516px;top:738px;width:189px;height:100px;background:linear-gradient(160deg,#5b9ad6,#aab3aa 45%,#7d867f)"></div>
  <ul class="abs checks orange" style="left:518px;top:861px;width:230px">
    <li><svg><use href="#tick"/></svg>Advanced Durability</li>
    <li><svg><use href="#tick"/></svg>A Bold First Impression</li>
    <li><svg><use href="#tick"/></svg>Longer Lasting Beauty</li>
    <li><svg><use href="#tick"/></svg>Realistic Woodgrain Textures</li>
    <li><svg><use href="#tick"/></svg>Vinyl</li>
  </ul>

  <!-- Gutters -->
  <h2 class="abs tab tab-left tab-orange" style="top:947px;width:174px">GUTTERS</h2>
  <p class="abs body-text body-left" style="top:994px">Compliment or beautifully contrast your home exterior with gutter toppers and rain-ware that lasts a lifetime. Roofing and Exteriors offers rain-ware that matches, complements or beautifully contrasts with your vinyl siding or color matches to your existing siding for a complete custom appearance.</p>
  <div class="abs photo orange" role="img" aria-label="Photo of a grey metal tile roof edge with a white gutter" style="left:272px;top:972px;width:189px;height:101px;background:linear-gradient(180deg,#4a8fd4,#aab4bd 45%,#8d959c 80%,#eef0f1)"></div>
  <ul class="abs checks orange" style="left:274px;top:1094px;width:200px">
    <li><svg><use href="#tick"/></svg>Aluminum And Stainless Steel Materials</li>
    <li><svg><use href="#tick"/></svg>Water Running Off</li>
    <li><svg><use href="#tick"/></svg>Gutter Toppers</li>
  </ul>

  <!-- Soffit / Fascia -->
  <h2 class="abs tab tab-right tab-blue" style="top:947px;width:242px">SOFFIT/FASCIA</h2>
  <p class="abs body-text body-right" style="top:994px">Soffit and fascia mentioned in the same breath. Together, this pair of roofing materials serves aesthetic and functional purposes. They cover unfinished structural parts of the roofline while protecting it from exposure to water, pests, and other potential damage.</p>
  <div class="abs photo" role="img" aria-label="Labelled diagram of a roof eave showing the fascia board and soffit" style="left:516px;top:972px;width:189px;height:101px;background:linear-gradient(160deg,#e8eef5,#c9d9ea 60%,#b7c9dc)"></div>
  <ul class="abs checks blue" style="left:518px;top:1094px;width:200px">
    <li><svg><use href="#tick"/></svg>Wood</li>
    <li><svg><use href="#tick"/></svg>Vinyl</li>
    <li><svg><use href="#tick"/></svg>Aluminum</li>
    <li><svg><use href="#tick"/></svg>Composite</li>
  </ul>
</main>
</body>
</html>
```